hi

i need an electronic store website designed. It should have light and warm colors like blue, green.

You will have to design the main page, product page, a normal page and also buttons and icons, boxes, etc. I will need the source files PSD/AI.

thanks

Electronic

```html
<!DOCTYPE html>
<html lang="en">
<head>
<meta charset="utf-8">
<title>Brightwave Electronics</title>
<link rel="stylesheet" href="https://fonts.googleapis.com/css2?family=Open+Sans:wght@400;600;700&family=Ubuntu:wght@400;500;700&display=swap">
<style>
:root{
  --sky:#00c8f0;
  --blue:#0a86c8;
  --navy:#084a78;
  --ink:#555;
  --title:#2a8fd0;
  --orange:#ff6a12;
  --white:#fff;
  --line:#e3e3e3;
  --placeholder:#d4dde5;
  --placeholder-soft:#e9eef2;
}
*{margin:0;padding:0;box-sizing:border-box}
html,body{width:960px;height:1200px;overflow:hidden;background:var(--white)}
body{position:relative;font-family:"Open Sans",Tahoma,sans-serif;color:var(--ink)}
.abs{position:absolute}
.header-bg{left:0;top:0;width:960px;height:280px;background:linear-gradient(180deg,var(--sky) 0%,#0aa6dc 40%,var(--blue) 100%)}
.cart-status{right:24px;top:8px;font-size:12px;color:#d9f6ff}
.logo{left:54px;top:48px}
.logo-name{font-weight:600;font-size:22px;color:var(--white);line-height:1}
.logo-tag{font-size:12px;color:#7fe6ff;margin-top:3px}
.nav{left:423px;top:60px;display:flex;height:44px}
.nav a{display:block;height:44px;line-height:44px;font-size:12px;color:#e8f8ff;text-decoration:none;text-align:center;border-left:1px solid rgba(255,255,255,.3)}
.nav a.active{background:linear-gradient(180deg,#40b4e6,#1a8fcc);border-top:3px solid #7ad8ff;line-height:40px;border-left:none;color:var(--white)}
.page{left:8px;top:115px;width:942px;height:950px;background:var(--white);border-radius:12px 12px 0 0}
.hero{left:0;top:118px;width:960px;height:300px}
.hero-title{left:97px;top:138px;font-family:"Ubuntu",sans-serif;font-size:22px;color:var(--white)}
.hero-rule{left:80px;top:165px;width:554px;height:1px;background:rgba(255,255,255,.5)}
.hero-img{background:rgba(255,255,255,.35);border-radius:3px}
.hero-label{font-family:"Ubuntu",sans-serif;font-weight:700;font-size:15px;color:var(--white);letter-spacing:.5px;display:flex;align-items:center;gap:14px}
.hero-label svg{flex:none}
.side-heading{font-family:"Ubuntu",sans-serif;font-size:18px;color:var(--title);left:52px}
.side-rule{left:40px;width:235px;height:16px}
.cat-list{left:55px;top:472px;width:210px;list-style:none}
.cat-list li{height:29px;line-height:29px;font-size:11px;color:#444;border-bottom:1px solid var(--line);padding-left:2px}
.cat-list li::before{content:"›";margin-right:5px;color:#777}
.search-input{left:50px;top:760px;width:180px;height:26px;border:1px solid #d8d8d8;background:#fbfbfb}
.advanced{left:49px;top:798px;font-size:11px;font-weight:700;color:#555;text-decoration:underline}
.btn{height:19px;line-height:19px;font-size:11px;font-weight:700;color:var(--white);text-align:center;border-radius:3px;text-transform:uppercase}
.btn-blue{background:linear-gradient(180deg,#3bb3e8,#137fc0);box-shadow:0 1px 2px rgba(0,0,0,.25)}
.btn-orange{background:linear-gradient(180deg,#ff8a2a,var(--orange));box-shadow:0 1px 2px rgba(0,0,0,.25)}
.info-list{left:58px;top:884px;list-style:none}
.info-list li{height:29px;font-size:11px;color:#444}
.product{width:280px;height:200px}
.product-thumb{left:0;top:0;width:116px;height:116px;border:2px solid #e6e6e6;background:var(--white)}
.product-thumb .shot{position:absolute;left:4px;top:4px;width:104px;height:104px;background:var(--placeholder-soft)}
.product-name{left:136px;top:4px;font-size:14px;color:var(--title)}
.product-desc{left:139px;top:27px;width:120px;font-size:12px;line-height:18.5px;color:#555}
.product-price{left:142px;top:110px;font-family:Georgia,serif;font-weight:700;font-size:13px;color:#555}
.footer-bar{left:0;top:1020px;width:960px;height:48px;background:var(--navy);border-top:2px solid #0e6aa8;color:#e6f2fa;font-size:11px;display:flex;align-items:center;padding-left:35px;gap:12px}
.footer-bar span.sep{color:#9cc}
.footer-main{left:0;top:1068px;width:960px;height:132px;background:linear-gradient(180deg,#0a6fae,var(--blue) 60%,#0a7fc0)}
.footer-col{top:1086px;font-size:11px;line-height:18.5px;color:#e8f5ff}
.footer-col h4{font-size:11px;font-weight:700;color:#4fd0ff;letter-spacing:.2px}
.card{top:1089px;width:45px;height:26px;background:linear-gradient(180deg,#fff,#dfe6ec);border-radius:3px;box-shadow:0 1px 2px rgba(0,0,0,.3)}
</style>
</head>
<body>
<div class="abs header-bg"></div>
<div class="abs cart-status">Shopping Cart items: 0 amount - $0.00</div>
<div class="abs logo">
  <div class="logo-name">Brightwave Electronics</div>
  <div class="logo-tag">shop with confidence</div>
</div>
<nav class="abs nav">
  <a class="active" style="width:75px">Home</a>
  <a style="width:89px;border-left:none">My Account</a>
  <a style="width:79px">Checkout</a>
  <a style="width:92px">Shopping Cart</a>
  <a style="width:92px">About Us</a>
  <a style="width:95px">Contact Us</a>
</nav>

<div class="abs page"></div>

<svg class="abs hero" viewBox="0 118 960 300" width="960" height="300">
  <defs>
    <linearGradient id="heroFill" x1="0" y1="0" x2="0" y2="1">
      <stop offset="0" stop-color="#2d9fd6"/>
      <stop offset=".35" stop-color="#41bde8"/>
      <stop offset="1" stop-color="#3fc0ec"/>
    </linearGradient>
    <linearGradient id="shade" x1="0" y1="0" x2="0" y2="1">
      <stop offset="0" stop-color="#c9c9c9" stop-opacity=".7"/>
      <stop offset="1" stop-color="#fff" stop-opacity="0"/>
    </linearGradient>
  </defs>
  <rect x="10" y="388" width="940" height="28" fill="url(#shade)"/>
  <rect x="31" y="125" width="896" height="243" fill="url(#heroFill)"/>
  <path d="M31 367 H58 L72 390 H262 L282 367 H378 L388 390 H573 L593 367 H664 L680 390 H866 L888 367 H927" fill="#41bde8"/>
</svg>
<div class="abs hero-title">Browse over 100 products from our store</div>
<div class="abs hero-rule"></div>
<div class="abs hero-img" role="img" aria-label="Photo of a flat-screen LCD monitor" style="left:60px;top:192px;width:218px;height:150px"></div>
<div class="abs hero-img" role="img" aria-label="Photo of a laptop" style="left:375px;top:190px;width:208px;height:158px"></div>
<div class="abs hero-img" role="img" aria-label="Photo of a remote control accessory" style="left:726px;top:188px;width:64px;height:158px"></div>
<div class="abs hero-label" style="left:77px;top:364px">
  <svg width="21" height="21" viewBox="0 0 21 21"><rect width="21" height="21" rx="5" fill="#ff8a1a"/><path d="M5 9h6V5l6 5.5-6 5.5v-4H5z" fill="#fff"/></svg>LCD MONITORS</div>
<div class="abs hero-label" style="left:395px;top:366px">
  <svg width="21" height="21" viewBox="0 0 21 21"><rect width="21" height="21" rx="5" fill="#ff8a1a"/><path d="M5 9h6V5l6 5.5-6 5.5v-4H5z" fill="#fff"/></svg>LAPTOPS</div>
<div class="abs hero-label" style="left:682px;top:366px">
  <svg width="21" height="21" viewBox="0 0 21 21"><rect width="21" height="21" rx="5" fill="#ff8a1a"/><path d="M5 9h6V5l6 5.5-6 5.5v-4H5z" fill="#fff"/></svg>ACCESSORIES</div>

<div class="abs side-heading" style="top:425px">CATEGORIES</div>
<svg class="abs side-rule" style="top:450px" viewBox="0 0 235 16"><path d="M0 1H60L68 9L76 1H235" fill="none" stroke="#e6e6e6" stroke-width="1.5"/></svg>
<ul class="abs cat-list">
  <li>Audio Systems</li><li>Cameras (1)</li><li>Computers (1)</li><li>Home Security (1)</li>
  <li>Home Theater (1)</li><li>Kitchen (1)</li><li>Mobile Phones</li><li>TV (2)</li>
</ul>
<div class="abs side-heading" style="top:714px">SEARCH</div>
<svg class="abs side-rule" style="top:739px" viewBox="0 0 235 16"><path d="M0 1H60L68 9L76 1H235" fill="none" stroke="#e6e6e6" stroke-width="1.5"/></svg>
<div class="abs search-input"></div>
<div class="abs advanced">advanced</div>
<div class="abs btn btn-blue" style="left:177px;top:798px;width:63px">Search</div>
<div class="abs side-heading" style="top:834px">INFORMATION</div>
<svg class="abs side-rule" style="top:859px" viewBox="0 0 235 16"><path d="M0 1H60L68 9L76 1H235" fill="none" stroke="#e6e6e6" stroke-width="1.5"/></svg>
<ul class="abs info-list"><li>Shipping</li><li>Privacy</li><li>About Us</li></ul>

<div class="abs product" style="left:339px;top:415px">
  <div class="abs product-thumb"><div class="shot" role="img" aria-label="Product photo of an LCD monitor"></div></div>
  <div class="abs product-name">product1</div>
  <div class="abs product-desc">Vivamus felis. Neges-tas ipsum. Fusce in Vivamus felis. Neges-tas ipsum. Fusce...</div>
  <div class="abs product-price">$33.00</div>
  <div class="abs btn btn-blue" style="left:5px;top:134px;width:85px">Add to cart</div>
  <div class="abs btn btn-orange" style="left:138px;top:136px;width:63px">Details</div>
</div>
<div class="abs product" style="left:624px;top:415px">
  <div class="abs product-thumb"><div class="shot" role="img" aria-label="Product photo of an LCD monitor"></div></div>
  <div class="abs product-name">product1</div>
  <div class="abs product-desc">Vivamus felis. Neges-tas ipsum. Fusce in Vivamus felis. Neges-tas ipsum. Fusce...</div>
  <div class="abs product-price">$33.00</div>
  <div class="abs btn btn-blue" style="left:5px;top:134px;width:85px">Add to cart</div>
  <div class="abs btn btn-orange" style="left:138px;top:136px;width:63px">Details</div>
</div>
<div class="abs product" style="left:339px;top:618px">
  <div class="abs product-thumb"><div class="shot" role="img" aria-label="Product photo of an LCD monitor"></div></div>
  <div class="abs product-name">product1</div>
  <div class="abs product-desc">Vivamus felis. Neges-tas ipsum. Fusce in Vivamus felis. Neges-tas ipsum. Fusce...</div>
  <div class="abs product-price">$33.00</div>
  <div class="abs btn btn-blue" style="left:5px;top:134px;width:85px">Add to cart</div>
  <div class="abs btn btn-orange" style="left:138px;top:136px;width:63px">Details</div>
</div>
<div class="abs product" style="left:624px;top:618px">
  <div class="abs product-thumb"><div class="shot" role="img" aria-label="Product photo of an LCD monitor"></div></div>
  <div class="abs product-name">product1</div>
  <div class="abs product-desc">Vivamus felis. Neges-tas ipsum. Fusce in Vivamus felis. Neges-tas ipsum. Fusce...</div>
  <div class="abs product-price">$33.00</div>
  <div class="abs btn btn-blue" style="left:5px;top:134px;width:85px">Add to cart</div>
  <div class="abs btn btn-orange" style="left:138px;top:136px;width:63px">Details</div>
</div>
<div class="abs product" style="left:339px;top:825px">
  <div class="abs product-thumb"><div class="shot" role="img" aria-label="Product photo of an LCD monitor"></div></div>
  <div class="abs product-name">product1</div>
  <div class="abs product-desc">Vivamus felis. Neges-tas ipsum. Fusce in Vivamus felis. Neges-tas ipsum. Fusce...</div>
  <div class="abs product-price">$33.00</div>
  <div class="abs btn btn-blue" style="left:5px;top:134px;width:85px">Add to cart</div>
  <div class="abs btn btn-orange" style="left:138px;top:136px;width:63px">Details</div>
</div>
<div class="abs product" style="left:624px;top:825px">
  <div class="abs product-thumb"><div class="shot" role="img" aria-label="Product photo of an LCD monitor"></div></div>
  <div class="abs product-name">product1</div>
  <div class="abs product-desc">Vivamus felis. Neges-tas ipsum. Fusce in Vivamus felis. Neges-tas ipsum. Fusce...</div>
  <div class="abs product-price">$33.00</div>
  <div class="abs btn btn-blue" style="left:5px;top:134px;width:85px">Add to cart</div>
  <div class="abs btn btn-orange" style="left:138px;top:136px;width:63px">Details</div>
</div>

<div class="abs footer-bar">
  <span>Copyright © 2013. All Rights Reserved. Storefront Themes</span>
  <span>Home</span><span class="sep">|</span><span>Shipping</span><span class="sep">|</span><span>Privacy</span><span class="sep">|</span><span>About Us</span>
</div>
<div class="abs footer-main"></div>
<div class="abs footer-col" style="left:37px">
  <h4>OFFICE INFORMATION:</h4>
  Brightwave Electronics<br>48 Harbor Lane<br>Riverton<br>Lakeshire,<br>10450, United States
</div>
<div class="abs footer-col" style="left:217px">
  <h4>CONTACT INFORMATION:</h4>
  Call us: (Int) 001 (55) 410 2087<br>Fax: (Int) 001 (55) 410 2087<br>Office hours: 8.00am - 4:00pm GMT+5
</div>
<div class="abs card" style="left:644px"></div>
<div class="abs card" style="left:700px"></div>
<div class="abs card" style="left:756px"></div>
<div class="abs card" style="left:812px"></div>
<div class="abs card" style="left:868px"></div>
</body>
</html>
```